Fashion Boutique shop and Fashion designer needs a business card (two in one)

This is a new business, I like light colors but very colorful. I would love attractive, one of a kind design :-)
On the back side I would like a white unicorn with rainbow color hair. On the back of the card around or under, not covering the unicorn I would like a quotation "Sometimes the smallest things take up the most room in your heart" Tibbet the Moss - or any lovely quote about love and gratitude.
Thank you very much.

Target Market(s)

Age 16-100 who loves unique clothing and shoes and lots of colours.

Industry/Entity Type

Business

Contact Information for Business Card

The boutique's name is Kit's Design
Mavis
027 385 9014
Boutique owner - Fashion designer
The Larchyard - Christchurch

Font styles to use
Script

Requirements
Must have
• some lovely dress or dresses, shoes, a woman with a nice colorful dress on, high heels or a dress as its getting made :-)

```html
<!DOCTYPE html>
<html lang="en">
<head>
<meta charset="utf-8">
<title>Mavis – Business Card</title>
<link rel="stylesheet" href="https://fonts.googleapis.com/css2?family=Cabin:wght@400;500&family=Dancing+Script:wght@600;700&display=swap">
<style>
  :root {
    --page: #ecebe8;
    --cream: #f7f1e6;
    --cream-deep: #ede2cf;
    --plum: #8e2a91;
    --plum-soft: #a24aa6;
    --tan: #d8c3a0;
    --ink: #231f20;
    --gold: #d9c29a;
    --sky: #dfe9f1;
    --sky-deep: #b9cfe0;
    --rose: #e6a3c8;
    --lilac: #b58ad0;
    --leaf: #cfe08a;
    --peach: #f2b27a;
  }
  * { box-sizing: border-box; margin: 0; padding: 0; }
  html, body { width: 1200px; height: 1000px; overflow: hidden; }
  body { background: var(--page); position: relative; font-family: "Cabin", sans-serif; }

  .card {
    position: absolute; left: 200px; width: 800px; height: 440px;
    overflow: hidden; border-radius: 4px;
    box-shadow: 0 6px 18px rgba(0,0,0,.12);
  }

  /* Back of card – quote side */
  .card-back { top: 40px; background: linear-gradient(160deg, #f4f7fa 0%, var(--sky) 45%, var(--sky-deep) 100%); }
  .unicorn-art {
    position: absolute; left: 90px; top: 50px; width: 660px; height: 350px;
    border-radius: 48% 52% 40% 45%;
    background:
      linear-gradient(90deg,
        rgba(233,76,90,.75) 0%, rgba(246,160,60,.75) 8%, rgba(250,220,80,.75) 14%,
        rgba(120,200,110,.7) 20%, rgba(90,150,230,.7) 26%, rgba(150,100,200,.6) 31%,
        rgba(255,255,255,.95) 40%, rgba(250,252,255,.95) 80%, rgba(230,238,246,.9) 100%);
    box-shadow: 0 0 40px 20px rgba(255,255,255,.45);
  }
  .back-corner {
    position: absolute; width: 220px; height: 140px;
    background: radial-gradient(ellipse at center, rgba(181,138,208,.7), rgba(230,163,200,.4) 50%, transparent 75%);
  }
  .back-corner.top-left { left: -40px; top: -50px; }
  .back-corner.bottom-right { right: -40px; bottom: -50px; background: radial-gradient(ellipse at center, rgba(110,90,200,.7), rgba(242,178,122,.4) 50%, transparent 75%); }

  .quote-panel {
    position: absolute; left: 250px; top: 110px; width: 480px; height: 200px;
    background: rgba(255,255,255,.8);
    display: flex; flex-direction: column; align-items: center; justify-content: center;
    text-align: center;
  }
  .quote-text {
    font-family: "Dancing Script", cursive; color: var(--plum);
    font-size: 31px; line-height: 1.15; font-weight: 700;
  }
  .quote-source { margin-top: 10px; font-size: 22px; color: var(--ink); }
  .quote-rule { margin-top: 6px; width: 60px; height: 3px; background: var(--plum); }

  /* Front of card – contact side */
  .card-front { top: 520px; background: radial-gradient(ellipse at 40% 30%, #fbf8f1 0%, var(--cream) 55%, var(--cream-deep) 100%); }
  .owner-name {
    position: absolute; left: 70px; top: 28px;
    font-family: "Dancing Script", cursive; font-weight: 700; font-size: 92px; color: var(--plum);
    line-height: 1;
  }
  .role-band { position: absolute; height: 38px; display: flex; align-items: center; font-size: 22px; }
  .role-band.boutique { left: 0; top: 140px; width: 335px; background: var(--tan); color: var(--ink); padding-left: 70px; }
  .role-band.designer { left: 335px; top: 178px; width: 210px; background: var(--ink); color: var(--gold); padding-left: 14px; }

  .contact-line {
    position: absolute; left: 48px; display: flex; align-items: center; gap: 10px;
    font-size: 27px; color: var(--ink);
  }
  .contact-line.phone { top: 184px; }
  .contact-line.address { top: 226px; }
  .contact-line svg { width: 20px; height: 22px; fill: var(--plum-soft); }

  .floral-wash {
    position: absolute; left: -30px; top: 260px; width: 330px; height: 220px;
    background:
      radial-gradient(ellipse 40% 35% at 60% 45%, rgba(207,224,138,.7), transparent 75%),
      radial-gradient(ellipse 35% 40% at 20% 60%, rgba(230,163,200,.6), transparent 75%),
      radial-gradient(ellipse 30% 30% at 35% 85%, rgba(242,178,122,.5), transparent 75%);
  }
  .floral-wash.corner {
    left: auto; right: -40px; top: auto; bottom: -60px; width: 240px; height: 150px;
    background: radial-gradient(ellipse at center, rgba(242,140,120,.6), rgba(181,138,208,.4) 50%, transparent 75%);
  }
  .shoe-art {
    position: absolute; left: 430px; top: 250px; width: 340px; height: 170px;
    border-radius: 40% 60% 10% 40%;
    background: linear-gradient(110deg, var(--lilac) 0%, var(--rose) 45%, #f0b3a0 75%, var(--lilac) 100%);
    opacity: .85;
  }
</style>
</head>
<body>

<section class="card card-back" aria-label="Card back">
  <div class="back-corner top-left" role="img" aria-label="Watercolour petal decoration"></div>
  <div class="back-corner bottom-right" role="img" aria-label="Watercolour petal decoration"></div>
  <div class="unicorn-art" role="img" aria-label="Illustration of a white winged unicorn with a rainbow mane and tail"></div>
  <div class="quote-panel">
    <p class="quote-text">Sometimes The Smallest Things Take<br>Up The Most Room In Your Heart</p>
    <p class="quote-source">Tibbet The Moss</p>
    <div class="quote-rule"></div>
  </div>
</section>

<section class="card card-front" aria-label="Card front">
  <div class="floral-wash" role="img" aria-label="Watercolour leaf and petal decoration"></div>
  <div class="floral-wash corner" role="img" aria-label="Watercolour petal decoration"></div>
  <div class="shoe-art" role="img" aria-label="Watercolour illustration of a high-heeled shoe"></div>

  <h1 class="owner-name">Mavis</h1>
  <div class="role-band boutique">Boutique owner</div>
  <div class="role-band designer">Fashion designer</div>

  <p class="contact-line phone">
    <svg viewBox="0 0 20 22" aria-hidden="true"><path d="M5 1c1 0 2 3 2.5 4.5S6 8 6 9s2.5 5 4 6 1.5-1.5 3-1 4 2 4 3-2 4-3.5 4C8 21 1 12 1 5 1 3 3.5 1 5 1z"/></svg>
    027 385 9014
  </p>
  <p class="contact-line address">
    <svg viewBox="0 0 20 22" aria-hidden="true"><path d="M10 1a7 7 0 0 0-7 7c0 5 7 13 7 13s7-8 7-13a7 7 0 0 0-7-7zm0 10a3 3 0 1 1 0-6 3 3 0 0 1 0 6z"/></svg>
    The Larchyard - Christchurch
  </p>
</section>

</body>
</html>
```